Vorlan cards

I am in the auto motive, transportation business I would like a business card that is Something cool, modern edgy, having to do with car culture. I offer towing service for high and exotic cars. I also provide towing for collisions and car accidents. I offer open and enclosed transport nationwide.

Target Market(s)

Car culture people high end auto collectors

Industry/Entity Type

Towing car carrier

Contact Information for Business Card

My company colors black yellow and silver

Font styles to use
Serif

```html
<!DOCTYPE html>
<html lang="en">
<head>
<meta charset="utf-8">
<title>Vorlan Transportation — Business Card</title>
<link href="https://fonts.googleapis.com/css2?family=Montserrat:wght@400;500;700;800&display=swap" rel="stylesheet">
<style>
  :root {
    --black: #0b0b0b;
    --ink: #111111;
    --yellow: #fde047;
    --yellow-deep: #f5d32a;
    --white: #ffffff;
    --silver: #c9c9cc;
    --muted: #e9e9eb;
    --backdrop: #d9d6d0;
  }
  * { box-sizing: border-box; margin: 0; padding: 0; }
  html, body {
    width: 900px; height: 1200px; overflow: hidden;
    background: var(--backdrop);
    font-family: "Montserrat", sans-serif;
  }
  .canvas { position: relative; width: 900px; height: 1200px; }

  .card {
    position: absolute; left: 80px; width: 742px; height: 443px;
    border-radius: 30px; overflow: hidden;
    box-shadow: 0 6px 14px rgba(0,0,0,.35);
  }

  /* Front */
  .card--front { top: 132px; background: var(--white); }
  .front__brand {
    position: absolute; left: 38px; top: 43px; width: 187px; height: 195px;
    display: flex; flex-direction: column; align-items: center; justify-content: center; gap: 10px;
    color: var(--ink); font-weight: 800; text-align: center; line-height: 1.05;
  }
  .brand__dot { width: 22px; height: 22px; border-radius: 50%; background: var(--yellow); }
  .brand__name { font-size: 34px; letter-spacing: 1px; text-transform: uppercase; }
  .brand__sub { font-size: 15px; letter-spacing: 1px; text-transform: uppercase; }

  .front__vehicle-art {
    position: absolute; left: 310px; top: 52px; width: 432px; height: 252px;
    background: linear-gradient(90deg, rgba(233,233,235,0) 0%, var(--muted) 35%, #f2f2f3 100%);
    border-radius: 40px 0 0 0;
  }
  .front__name-band {
    position: absolute; left: 0; top: 268px; width: 262px; height: 58px;
    background: var(--yellow);
    clip-path: polygon(0 0, 235px 0, 262px 100%, 0 100%);
    padding: 6px 0 0 27px;
  }
  .person__name { font-size: 26px; font-weight: 700; color: var(--ink); line-height: 1.1; }
  .person__role { font-size: 15px; font-weight: 500; color: var(--ink); }
  .front__stripe {
    position: absolute; left: 260px; right: 0; top: 304px; height: 12px;
    background: var(--black);
    clip-path: polygon(0 0, 100% 0, 100% 100%, 6px 100%);
  }
  .front__footer {
    position: absolute; left: 0; right: 0; top: 326px; bottom: 0;
    background: var(--black); color: var(--white);
  }
  .contact-list { position: absolute; left: 27px; top: 25px; list-style: none; }
  .contact-list li {
    display: flex; align-items: center; gap: 10px;
    font-size: 16px; height: 21.5px;
  }
  .contact-list svg { width: 14px; height: 14px; fill: var(--white); }
  .address {
    position: absolute; left: 502px; top: 50px; height: 32px;
    border-left: 2px solid var(--yellow); padding-left: 19px;
    font-size: 16px; line-height: 21px; font-style: normal;
    display: flex; flex-direction: column; justify-content: center;
  }

  /* Back */
  .card--back { top: 638px; background: var(--ink); }
  .back__vehicle-art {
    position: absolute; left: 350px; top: 50px; width: 392px; height: 375px;
    background: radial-gradient(ellipse at 70% 45%, #3a3a3d 0%, #242426 45%, rgba(17,17,17,0) 75%);
  }
  .back__brand {
    position: absolute; left: 215px; top: 62px; width: 300px; height: 310px;
    display: flex; flex-direction: column; align-items: center; justify-content: center; gap: 14px;
    color: var(--yellow); font-weight: 800; text-align: center; line-height: 1.05;
  }
  .back__brand .brand__name { font-size: 54px; }
  .back__brand .brand__sub { font-size: 22px; }
  .back__band {
    position: absolute; left: 0; right: 0; bottom: 0; height: 12px; background: var(--yellow);
  }
</style>
</head>
<body>
<main class="canvas">

  <section class="card card--front" aria-label="Business card front">
    <div class="front__vehicle-art" role="img" aria-label="Faint flatbed tow truck illustration"></div>

    <div class="front__brand">
      <span class="brand__dot"></span>
      <span class="brand__name">Vorlan</span>
      <span class="brand__sub">Transportation</span>
    </div>

    <div class="front__name-band">
      <p class="person__name">Dana Reyes</p>
      <p class="person__role">Owner</p>
    </div>
    <div class="front__stripe"></div>

    <div class="front__footer">
      <ul class="contact-list">
        <li>
          <svg viewBox="0 0 16 16" aria-hidden="true"><path d="M3 2h3l1.5 3.5-2 1.2a8 8 0 0 0 3.8 3.8l1.2-2L14 10v3a1 1 0 0 1-1 1A11 11 0 0 1 2 3a1 1 0 0 1 1-1z"/></svg>
          (555) 014-2290
        </li>
        <li>
          <svg viewBox="0 0 16 16" aria-hidden="true"><path d="M1 3h14v10H1z M1.5 3.5 8 9l6.5-5.5" stroke="#0b0b0b" stroke-width="1.2"/></svg>
          info@vorlantransport.com
        </li>
        <li>
          <svg viewBox="0 0 16 16" aria-hidden="true"><circle cx="8" cy="8" r="7"/><path d="M1 8h14M8 1c3 3 3 11 0 14M8 1c-3 3-3 11 0 14" stroke="#0b0b0b" stroke-width="1" fill="none"/></svg>
          www.vorlantransport.com
        </li>
      </ul>
      <address class="address">
        <span>48 Harbor Lane</span>
        <span>Millbrook, PA 17000</span>
      </address>
    </div>
  </section>

  <section class="card card--back" aria-label="Business card back">
    <div class="back__vehicle-art" role="img" aria-label="Large dark tow truck silhouette"></div>
    <div class="back__brand">
      <span class="brand__name">VORLAN</span>
      <span class="brand__sub">Transportation</span>
    </div>
    <div class="back__band"></div>
  </section>

</main>
</body>
</html>
```